Medical Internet Marketing Company Needs a Site!

We need a new, fresh website for our search engine optimization and social media marketing company. We specialize in helping medical practices, doctors, physicians, and hospitals with their online presence and web ranking. The site should lean towards being suited for these audiences.

We have several examples of website that we like as well as things that we like about them.

Here are sites that we enjoy.

www.brightwavepromo.com

It's a good design for the site all around. The videos, buttons, and images are all excellent. They did a fine job.

- We really like their "contact us" side bar and want to include one like it on the secondary pages.

www.kestrelgrow.net

- We don't like the "thickness" of the top navigation bar.
- We like the page colors, easy navigation, and big call to action phone number in the top right corner.

http://www.tulavo.com/

Out of all the examples provided, Tulavo is our favorite and closest look and style to what we are looking for.

- We really like the openness of the design, such as space between the text and background.

- We want a price page in a style very similar to their pricing page with the services listed and check-marks, etc. although we intend to have multiple service package columns much like Kestrel's SEO pricing page.

- The way the video fits into the home page header is very organized, simple, and attention grabbing. We intend to place a slider with videos here.

- We need a page design that will allow for an image slider like Tulavo's Features page.

Here's a great example of a medical internet marketing website: http://www.dorvanta.com/

Target Market(s)

Our target market is doctors, typically male and typically 40-45 years old. I

Industry/Entity Type

Marketing

Requirements
Must have
• The homepage should have a slider in the video. Interior pages should have a video in the very top similar to how they do it on www.brightwavepromo.com

The top navigation tabs needed are:
- Home
- Solutions
- Resources
- About
- Why Zentrol
- Contact

The sidebar should have a GREAT call to action in it on interior pages.

There should be one interior page that is similar to this - http://www.tulavo.com/pricing/

There needs to be a page with multiple boxes that take up a row of the web page's body. This page will house all the case studies similar to brightwave promo's: http://www.brightwavepromo.com/success-stories/case-studies/ The one exception is we want the case studies to be inside of "boxes" instead of between horizontal lines like brightwave promo's.
Nice to have
• Color, professional, and clean. GREAT use of calls to actions.

```html
<!DOCTYPE html>
<html lang="en">
<head>
<meta charset="utf-8">
<title>Zentrol – Medical Internet Marketing Packages</title>
<link rel="stylesheet" href="https://fonts.googleapis.com/css2?family=Ubuntu:wght@500;700&family=Arimo:wght@400;700&display=swap">
<style>
:root{
  --page:#ffffff;
  --canvas:#f2f2f2;
  --frame-top:#7a7a7a;
  --ink:#4a4a4a;
  --nav:#8a8a8a;
  --band:#3e84b5;
  --green:#7ab929;
  --green-dark:#5e9a17;
  --sky:#8fd3f3;
  --gold:#d1a12c;
  --head-gray:#9b9fa3;
  --row-alt:#f5f5f5;
  --rule:#e2e2e2;
  --tick:#7dbb22;
  --cross:#e2561b;
  --footer:#7c7c7c;
  --footer-link:#9fd9f5;
  --bottom:#2c2c2c;
}
*{box-sizing:border-box;margin:0;padding:0}
html,body{width:993px;height:1200px;overflow:hidden;background:var(--canvas)}
body{position:relative;font-family:"Arimo",Arial,sans-serif;color:var(--ink)}
.page{position:absolute;left:25px;top:26px;width:944px;height:1160px;background:var(--page);border:1px solid #cfcfcf;overflow:hidden}
.page > *{position:absolute}
.top-rule{left:0;top:0;width:100%;height:7px;background:var(--frame-top)}
.header{left:0;top:7px;width:100%;height:68px;border-bottom:1px solid #d8d8d8}
.brand{position:absolute;left:152px;top:27px;display:flex;align-items:center;gap:10px}
.brand-mark{width:24px;height:24px;background:var(--green)}
.brand-name{font-family:"Ubuntu",sans-serif;font-weight:500;font-size:30px;letter-spacing:2px;color:#8c8c8c}
.call{position:absolute;left:603px;top:0;width:117px;height:24px;background:var(--green);color:#fff;font-weight:700;font-size:15px;display:flex;align-items:center;justify-content:center;gap:6px}
.social{position:absolute;top:2px;display:flex;gap:6px;left:728px}
.social span{width:17px;height:17px;display:block}
.nav{position:absolute;top:38px;left:398px;display:flex;font-size:12px;font-weight:700;color:var(--nav)}
.nav a{color:inherit;text-decoration:none;margin-right:26px}
.nav a:last-child{margin-right:0}
.hero-band{left:0;top:77px;width:100%;height:186px;background:var(--band)}
.hero{position:absolute;left:143px;top:7px;width:657px;height:169px;background:#fff}
.hero h1{position:absolute;left:19px;top:14px;font-family:"Ubuntu",sans-serif;font-weight:700;font-size:29px;line-height:34px;color:var(--green);white-space:nowrap}
.hero h1 span{color:var(--sky);display:block}
.hero p{position:absolute;left:19px;top:86px;font-size:10.5px;font-weight:700;line-height:15px;color:#555;white-space:nowrap}
.btn-cta{position:absolute;left:19px;top:124px;width:130px;height:23px;background:var(--green);color:#fff;font-size:11px;font-weight:700;display:flex;align-items:center;justify-content:center}
.hero-art{position:absolute;left:395px;top:8px;width:238px;height:161px;background:linear-gradient(135deg,#f7efe2,#efe1c8);border:2px solid #222}
.section-title{left:155px;top:288px;font-size:10.5px;font-weight:700;color:var(--green)}
.pricing{left:148px;top:313px;width:647px;border:1px solid var(--rule);border-radius:6px;overflow:hidden;border-collapse:collapse;table-layout:fixed;font-size:10.5px}
.pricing th{height:55px;color:#fff;text-align:left;font-family:"Ubuntu",sans-serif;font-weight:500;vertical-align:middle}
.pricing .details{background:var(--head-gray);width:196px;padding:0 15px;font-size:14px;font-weight:400}
.plan{position:relative;padding-left:11px;font-size:16px;line-height:17px}
.plan b{position:absolute;right:11px;top:3px;font-size:32px;font-weight:700}
.plan b small{font-size:17px}
.plan i{position:absolute;right:15px;bottom:7px;font-style:normal;font-size:7px;font-family:"Arimo",sans-serif}
.basic{background:var(--sky);width:147px}
.pro{background:var(--green);width:150px}
.premium{background:var(--gold);width:154px}
.pricing td{height:27px;border-top:1px solid var(--rule);border-left:1px solid var(--rule);text-align:center}
.pricing td:first-child{border-left:0;text-align:left;padding-left:14px}
.pricing tbody tr:nth-child(odd){background:var(--row-alt)}
.pricing td svg{width:14px;height:12px;vertical-align:middle}
.pricing tfoot td{height:47px;background:#fafafa}
.enquire{display:inline-block;width:106px;height:22px;line-height:22px;color:#fff;font-weight:700;font-size:11px}
.e-basic{background:var(--sky)}.e-pro{background:var(--green)}.e-premium{background:var(--gold)}
.expert-bar{left:148px;top:876px;width:647px;height:23px;background:var(--sky);color:#fff;font-weight:700;font-size:12px;display:flex;align-items:center;padding-left:24px;gap:6px;white-space:nowrap}
.expert-bar strong{font-size:16px}
.footer{left:0;top:923px;width:100%;height:201px;background:var(--footer);color:#f0f0f0;font-size:8px}
.footer h4{font-size:8px;font-weight:700;color:#fff;padding-bottom:6px;border-bottom:1px solid #999}
.f-nav{position:absolute;left:156px;top:21px;width:150px}
.f-nav-links{position:absolute;left:155px;top:44px;white-space:nowrap}
.f-nav-links span{margin:0 6px}
.f-tweets{position:absolute;left:156px;top:69px;width:312px}
.tweet{margin-top:12px;padding-left:2px;line-height:12px}
.tweet em{color:var(--footer-link)}
.f-res{position:absolute;left:478px;top:21px;width:311px}
.res{margin-top:10px;line-height:11px}
.res b{color:var(--footer-link);display:block}
.f-cta{position:absolute;left:480px;top:152px;width:262px;height:23px;background:var(--sky);color:#fff;font-weight:700;font-size:10.5px;display:flex;align-items:center;justify-content:center;gap:5px;white-space:nowrap}
.f-cta strong{font-size:15px}
.bottom{left:0;top:1124px;width:100%;height:36px;background:var(--bottom);color:#555;font-size:8px}
.bottom .copy{position:absolute;left:152px;top:12px}
.bottom .top{position:absolute;left:762px;top:12px}
</style>
</head>
<body>
<svg width="0" height="0" style="position:absolute">
  <defs>
    <symbol id="tick" viewBox="0 0 14 12"><path d="M1 6.5l4 4L13 2" fill="none" stroke="#7dbb22" stroke-width="3" stroke-linecap="round" stroke-linejoin="round"/></symbol>
    <symbol id="cross" viewBox="0 0 14 12"><path d="M3 2l8 8M11 2l-8 8" stroke="#e2561b" stroke-width="3" stroke-linecap="round"/></symbol>
    <symbol id="phone" viewBox="0 0 16 12"><path d="M1 4c0-2 3-3 7-3s7 1 7 3v1h-3V4H4v1H1zM4 6h8l2 5H2z" fill="#fff"/></symbol>
  </defs>
</svg>
<div class="page">
  <div class="top-rule"></div>
  <header class="header">
    <div class="brand"><span class="brand-mark"></span><span class="brand-name">ZENTROL</span></div>
    <div class="call"><svg width="14" height="11"><use href="#phone"/></svg>08-555-0142</div>
    <div class="social"><span style="background:#3b5b98"></span><span style="background:#4fb5e6"></span><span style="background:#1b74b0"></span></div>
    <nav class="nav"><a>Home</a><a>Solutions</a><a>Resources</a><a>About</a><a>Why Zentrol</a><a>Contact</a></nav>
  </header>
  <section class="hero-band">
    <div class="hero">
      <h1>Simple Easy Predictable <span>Marketing Pricing Plan</span></h1>
      <p>We have packages that are tailoured especially for you or your<br>practice. Attracting new patients does not have to cost the earth</p>
      <div class="btn-cta">GET IN TOUCH TODAY</div>
      <div class="hero-art" role="img" aria-label="Illustration of a cheerful cartoon doctor pointing at a rising 'New Patients' chart"></div>
    </div>
  </section>
  <h2 class="section-title">OUR MEDICAL INTERNET MARKETING PACKAGES</h2>
  <table class="pricing">
    <thead><tr>
      <th class="details">Our Package Details</th>
      <th class="plan basic">Basic<br>Package<b>10<small>$</small></b><i>per month</i></th>
      <th class="plan pro">Pro<br>Package<b>20<small>$</small></b><i>per month</i></th>
      <th class="plan premium">Premuim<br>Package<b>35<small>$</small></b><i>per month</i></th>
    </tr></thead>
    <tbody>
      <tr><td>Lorem ipsum est dolor</td><td><svg><use href="#tick"/></svg></td><td><svg><use href="#tick"/></svg></td><td><svg><use href="#tick"/></svg></td></tr>
      <tr><td>Lorem ipsum est dolor</td><td><svg><use href="#tick"/></svg></td><td><svg><use href="#tick"/></svg></td><td><svg><use href="#tick"/></svg></td></tr>
      <tr><td>Lorem ipsum est dolor</td><td><svg><use href="#tick"/></svg></td><td><svg><use href="#tick"/></svg></td><td><svg><use href="#tick"/></svg></td></tr>
      <tr><td>Lorem ipsum est dolor amet</td><td><svg><use href="#cross"/></svg></td><td><svg><use href="#tick"/></svg></td><td><svg><use href="#tick"/></svg></td></tr>
      <tr><td>Lorem ipsum est dolor</td><td><svg><use href="#tick"/></svg></td><td><svg><use href="#tick"/></svg></td><td><svg><use href="#tick"/></svg></td></tr>
      <tr><td>Lorem ipsum est dolor</td><td><svg><use href="#cross"/></svg></td><td><svg><use href="#tick"/></svg></td><td><svg><use href="#tick"/></svg></td></tr>
      <tr><td>Lorem ipsum est dolor amet</td><td><svg><use href="#cross"/></svg></td><td><svg><use href="#cross"/></svg></td><td><svg><use href="#tick"/></svg></td></tr>
      <tr><td>Lorem ipsum</td><td><svg><use href="#tick"/></svg></td><td><svg><use href="#cross"/></svg></td><td><svg><use href="#tick"/></svg></td></tr>
      <tr><td>Lorem ipsum est dolor</td><td><svg><use href="#tick"/></svg></td><td><svg><use href="#tick"/></svg></td><td><svg><use href="#tick"/></svg></td></tr>
      <tr><td>Lorem ipsum est dolor</td><td><svg><use href="#tick"/></svg></td><td><svg><use href="#tick"/></svg></td><td><svg><use href="#tick"/></svg></td></tr>
      <tr><td>Lorem ipsum est dolor</td><td><svg><use href="#tick"/></svg></td><td><svg><use href="#tick"/></svg></td><td><svg><use href="#tick"/></svg></td></tr>
      <tr><td>Lorem ipsum est dolor amet</td><td><svg><use href="#tick"/></svg></td><td><svg><use href="#tick"/></svg></td><td><svg><use href="#tick"/></svg></td></tr>
      <tr><td>Lorem ipsum est dolor</td><td><svg><use href="#cross"/></svg></td><td><svg><use href="#tick"/></svg></td><td><svg><use href="#tick"/></svg></td></tr>
      <tr><td>Lorem ipsum est dolor amet</td><td><svg><use href="#tick"/></svg></td><td><svg><use href="#tick"/></svg></td><td><svg><use href="#tick"/></svg></td></tr>
      <tr><td>Lorem ipsum est dolor</td><td><svg><use href="#cross"/></svg></td><td><svg><use href="#cross"/></svg></td><td><svg><use href="#tick"/></svg></td></tr>
      <tr><td>Lorem ipsum est dolor</td><td><svg><use href="#tick"/></svg></td><td><svg><use href="#tick"/></svg></td><td><svg><use href="#tick"/></svg></td></tr>
    </tbody>
    <tfoot><tr><td></td><td><span class="enquire e-basic">ENQUIRE NOW</span></td><td><span class="enquire e-pro">ENQUIRE NOW</span></td><td><span class="enquire e-premium">ENQUIRE NOW</span></td></tr></tfoot>
  </table>
  <div class="expert-bar">SPEAK TO AN EXPERT NOW AND SEE HOW WE CAN BRING YOU NEW PATIENTS <svg width="15" height="11"><use href="#phone"/></svg><strong>08-555-0142</strong></div>
  <footer class="footer">
    <div class="f-nav"><h4>NAVIGATION</h4></div>
    <div class="f-nav-links">Home<span>|</span>Solutions<span>|</span>Resources<span>|</span>About<span>|</span>Why Zentrol<span>|</span>Contact</div>
    <div class="f-tweets">
      <h4>@Zentrol</h4>
      <p class="tweet">Vestibulum ante ipsum primis in faucibus #orci luctus et ultrices posuere cubilia Curaesed eu nibh <em>#phasellus</em> vitae mi in mollis turpis ipsum.<br><em>22 minutes ago</em> via <em>Chirper</em></p>
      <p class="tweet">Vestibulum ante ipsum primis in faucibus #orci luctus et ultrices posuere cubilia Curaesed eu nibh <em>#phasellus</em> vitae mi in mollis turpis ipsum.<br><em>22 minutes ago</em> via <em>Chirper</em></p>
    </div>
    <div class="f-res">
      <h4>RECENTLY ADDED RESOURCES</h4>
      <p class="res"><b>Vestibulum ante ipsum primis</b>Phasellus mollis turpis ipsum. Aenean vitae mi in est pulvinar ornare.</p>
      <p class="res"><b>Vestibulum ante ipsum primis</b>Phasellus mollis turpis ipsum. Aenean vitae mi in est pulvinar ornare.</p>
      <p class="res"><b>Vestibulum ante ipsum primis</b>Phasellus mollis turpis ipsum. Aenean vitae mi in est pulvinar ornare.</p>
    </div>
    <div class="f-cta">SPEAK TO AN EXPERT TODAY! <strong>08-555-0142</strong></div>
  </footer>
  <div class="bottom"><span class="copy">© Copyright 2012 - Zentrol</span><span class="top">TOP ▲</span></div>
</div>
</body>
</html>
```